Envelope Design Project for Real Estate

I am looking for an envelope design for a real estate brokerage. I prefer muted colors and the primary colors should be white, maroon (884445) and gray (aaaaaa).
The design is for a #10 universal envelope (psd and jpg files attached for guidelines). There should be full color on the front and back of the envelope.
You can add a return address on the back side along the top flap. Please use a sample address and phone number in the design - the actual information will be provided to the winning designer.
Industry/Entity Type
Real Estate
Look and feel
Each slider illustrates characteristics of the customer's brand and the style your logo design should communicate.

```html
<!DOCTYPE html>
<html lang="en">
<head>
<meta charset="utf-8">
<title>Oak Harbor Real Estate – #10 Envelope, Back</title>
<link rel="stylesheet" href="https://fonts.googleapis.com/css2?family=Open+Sans:wght@400&display=swap">
<style>
  :root {
    --maroon: #834042;
    --maroon-flap: #7f3f41;
    --gray: #aaaaaa;
    --white: #ffffff;
    --page: #ffffff;
  }
  html, body {
    margin: 0;
    padding: 0;
    width: 1200px;
    height: 662px;
    overflow: hidden;
    background: var(--page);
  }
  .envelope {
    display: block;
    width: 1200px;
    height: 662px;
  }
  .flap { fill: var(--maroon-flap); }
  .body-paper { fill: var(--white); stroke: #e4e4e4; stroke-width: 1; }
  .gray-band { fill: var(--gray); }
  .maroon-panel { fill: var(--maroon); }
  .brand-mark { fill: none; stroke: var(--white); stroke-width: 4; }
  .brand-name {
    font-family: "Open Sans", sans-serif;
    font-weight: 400;
    fill: var(--white);
  }
  .brand-name__main { font-size: 27px; letter-spacing: 1px; }
  .brand-name__sub { font-size: 11px; letter-spacing: 3.5px; }
  .return-address {
    font-family: "Open Sans", sans-serif;
    font-weight: 400;
    font-size: 18px;
    fill: var(--white);
  }
</style>
</head>
<body>
<svg class="envelope" viewBox="0 0 1200 662" xmlns="http://www.w3.org/2000/svg">
  <!-- top flap -->
  <polygon class="flap" points="54,26 1146,26 1170,136 30,136"/>

  <!-- envelope body -->
  <rect class="body-paper" x="30" y="136" width="1140" height="496"/>

  <!-- gray sweep -->
  <path class="gray-band" d="M30,136 L662,136 Q900,330 1010,632 L30,632 Z"/>
  <!-- maroon panel with thin white gap -->
  <path class="maroon-panel" d="M30,136 L641,136 Q870,330 985,632 L30,632 Z"/>
  <path d="M645,136 Q876,330 991,632" fill="none" stroke="var(--white)" stroke-width="4"/>

  <!-- brand -->
  <circle class="brand-mark" cx="147" cy="207" r="42"/>
  <text class="brand-name brand-name__main" x="147" y="267" text-anchor="middle">OAK HARBOR</text>
  <text class="brand-name brand-name__sub" x="147" y="282" text-anchor="middle">REAL ESTATE</text>

  <!-- return address -->
  <text class="return-address" x="68" y="572">Lena Varga, Lindenhof-Gasse 12/B204, 1130 Wien</text>
  <text class="return-address" x="68" y="597">Tel.:&#160;&#160;+43 699 000 481 27, hello@oakharbor-homes.com, www.oakharbor-homes.com</text>
</svg>
</body>
</html>
```